CTWI application splash screen

We need a 1024x768 image for use as an application splash screen.
The image will be displayed full screen on an 10 inch industrial PC 1024x768 screen while our application is launching. The image should convey that the application is "Waiting for connection to Wi-Fi access point..." and include a graphic of the industrial PC connected to the access point via an Ethernet cable. A list of troubleshooting steps should be included at the bottom of the image. The troubleshooting steps should not be the main focus of the image and should be shown in a smaller font (but still readable at 1024x768 displayed on a 10 inch screen).
I will include a mock up of the general idea of what we are looking for as well as image files for the industrial PC, a screenshot of our application to show on the PC's screen and the AP.
For general look and feel and a sense of corporate branding please review our website https://corvanetillageworks.com/. The splash screen should reflect corporate branding.
Target Market(s)
Users of our application
Industry/Entity Type
Agriculture

```html
<!DOCTYPE html>
<html lang="en">
<head>
<meta charset="UTF-8">
<title>CTWI – Waiting for Wi-Fi access point</title>
<link rel="stylesheet" href="https://fonts.googleapis.com/css2?family=Quicksand:wght@500;700&family=Tinos&display=swap">
<style>
  :root {
    --page-bg: #000000;
    --green-top: #23985e;
    --green-mid: #167246;
    --green-bottom: #0c2215;
    --text-light: #ffffff;
    --pill-bg: rgba(180, 200, 188, 0.55);
    --card-bg: rgba(190, 205, 196, 0.5);
    --device-body: #2b2b2b;
    --device-screen: #e9efe9;
    --ap-white: #f1f1f1;
  }
  * { margin: 0; padding: 0; box-sizing: border-box; }
  html, body { width: 1200px; height: 1200px; overflow: hidden; background: var(--page-bg); }
  .splash {
    position: absolute; left: 0; top: 150px; width: 1200px; height: 900px;
    background: linear-gradient(180deg, var(--green-top) 0%, var(--green-mid) 45%, var(--green-bottom) 100%);
    color: var(--text-light); font-family: "Quicksand", sans-serif;
  }
  .splash-title {
    position: absolute; top: 54px; width: 100%; text-align: center;
    font-weight: 700; font-size: 43px; letter-spacing: 0.3px;
  }
  .device-pc {
    position: absolute; left: 47px; top: 164px; width: 352px; height: 280px;
    border-radius: 14px; background: var(--device-body);
    padding: 26px 40px 52px 30px;
  }
  .device-pc .screen {
    width: 100%; height: 100%;
    background: linear-gradient(180deg, var(--device-screen), #cfe4d4);
  }
  .device-ap {
    position: absolute; left: 1033px; top: 143px; width: 41px; height: 304px;
    background: linear-gradient(90deg, #d6d6d6, var(--ap-white) 50%, #d0d0d0);
    border-radius: 10px;
  }
  .link-diagram { position: absolute; left: 0; top: 0; }
  .label { position: absolute; text-align: center; font-weight: 700; font-size: 28px; line-height: 34px; }
  .label-pc { left: 99px; width: 200px; top: 542px; }
  .label-ap { left: 897px; width: 300px; top: 542px; }
  .label-ap .model { display: block; font-weight: 500; font-size: 21px; line-height: 28px; }
  .cable-name {
    position: absolute; left: 440px; width: 400px; top: 497px; text-align: center;
    font-weight: 700; font-size: 27px; letter-spacing: 1.5px;
  }
  .troubleshooting { font-family: "Tinos", serif; }
  .trouble-heading {
    position: absolute; left: 54px; top: 657px; width: 239px; height: 37px;
    background: var(--pill-bg); border-radius: 6px;
    font-size: 21px; line-height: 37px; padding-left: 10px;
  }
  .trouble-list { position: absolute; left: 59px; top: 705px; list-style: none; font-size: 19px; }
  .trouble-list li { height: 37px; display: flex; align-items: center; gap: 6px; }
  .trouble-list li::before {
    content: ""; width: 13px; height: 13px; border: 1.5px solid var(--text-light); border-radius: 50%;
  }
  .step-card {
    position: absolute; top: 781px; height: 96px; background: var(--card-bg);
    border-radius: 6px; padding: 9px 14px; font-size: 16.5px; line-height: 20.5px;
  }
  .step-1 { left: 79px; width: 277px; }
  .step-2 { left: 371px; width: 278px; }
  .step-3 { left: 666px; width: 241px; }
  .step-4 { left: 923px; width: 241px; }
</style>
</head>
<body>
<main class="splash">
  <h1 class="splash-title">Waiting for Connection to Wi-Fi access point...</h1>

  <div class="device-pc" role="img" aria-label="Industrial tractor cab computer showing the CTWI application screen">
    <div class="screen"></div>
  </div>
  <div class="device-ap" role="img" aria-label="White outdoor Wi-Fi access point with two antennas"></div>

  <svg class="link-diagram" width="1200" height="900" viewBox="0 0 1200 900" aria-hidden="true">
    <g fill="none" stroke="#ffffff" stroke-width="4" stroke-linecap="round" stroke-dasharray="0.1 9">
      <path d="M214 472 V513 H503"/>
      <path d="M1053 472 V513 H776"/>
    </g>
    <circle cx="214" cy="457" r="10" fill="#0d2a1a" stroke="#ffffff" stroke-width="3"/>
    <circle cx="1053" cy="457" r="10" fill="#0d2a1a" stroke="#ffffff" stroke-width="3"/>
  </svg>
  <div class="cable-name">ETHERNET CABLE</div>

  <div class="label label-pc">Tractor cab computer</div>
  <div class="label label-ap">Wi-Fi Access Point<span class="model">Fennick WAP330-Outdoor</span></div>

  <section class="troubleshooting">
    <h2 class="trouble-heading" style="font-weight:400">Troubleshooting steps:</h2>
    <ul class="trouble-list">
      <li>This screen should only be visible for a short time on boot.</li>
      <li>If this screen stays visible for more than a minute:</li>
    </ul>
    <p class="step-card step-1">Verify that the Wi-Fi Access Point (AP) powers up when this system does (indicated by a green light n the side of the AP).</p>
    <p class="step-card step-2">Check the Ethernet cable between this system and the AP for damage, and replace it if necessary.</p>
    <p class="step-card step-3">Power-cycle this system and wait for it to reboot fully.</p>
    <p class="step-card step-4">If the issue persists, contact CTWI support for further assistance.</p>
  </section>
</main>
</body>
</html>
```